Waste management company seeks a new website design

We need a website design for an environmental services company called 'Vilumetsa Kogumisteenused.' We manage waste collection and recycling for 100K+ households and businesses across Estonia. Please use logos and colors from attached CVI file. The design should be extensively usable for our self-service portal and have a mobile-first approach as it will be turned into an app in the future. The new website should highlight our commitment to sustainability and provide easy access to our services with a clean, modern design. UX inspiration from https://trevix.eu/et-ee/

```html
<!DOCTYPE html>
<html lang="et">
<head>
<meta charset="utf-8">
<title>Vilumetsa Kogumisteenused – veebileht</title>
<link href="https://fonts.googleapis.com/css2?family=Fira+Sans:wght@400;500;600;700&family=PT+Sans:wght@400;700&display=swap" rel="stylesheet">
<style>
:root{
  --brown:#7a6d63;
  --brown-dark:#5e534b;
  --lime:#cddc2b;
  --white:#ffffff;
  --paper:#e4e3e3;
  --card:#f3f3f3;
  --ink:#2b2623;
  --muted:#8a8a8a;
}
*{box-sizing:border-box;margin:0;padding:0}
html,body{width:1170px;height:1200px;overflow:hidden}
body{background:var(--paper);font-family:"PT Sans",sans-serif;color:var(--ink);position:relative}
.heading{font-family:"Fira Sans",sans-serif}

/* Desktop page */
.desktop{position:absolute;left:60px;top:30px;width:1050px;height:626px;background:var(--brown);overflow:hidden;color:var(--white)}
.brand{position:absolute;left:47px;top:38px;display:flex;align-items:center;gap:10px}
.brand-dot{width:30px;height:30px;border-radius:50%;background:var(--lime)}
.brand-name{font-family:"Fira Sans",sans-serif;font-size:15px;font-weight:500;line-height:1.05;color:var(--white)}
.main-nav{position:absolute;left:368px;top:51px;display:flex;gap:18px;font-family:"Fira Sans",sans-serif;font-size:8px;font-weight:600}
.lang{position:absolute;left:808px;top:44px;display:flex;align-items:center;gap:6px;font-size:9px;font-weight:700}
.flag{width:22px;height:22px;border-radius:50%;overflow:hidden;border:1.5px solid var(--white);background:linear-gradient(#1d7fd1 0 33%,#111 33% 66%,#fff 66%)}
.portal-btn{position:absolute;left:890px;top:37px;width:110px;height:32px;border-radius:16px;background:var(--white);color:var(--ink);font-family:"Fira Sans",sans-serif;font-size:8px;font-weight:700;display:flex;align-items:center;justify-content:center}
.hero-title{position:absolute;left:0;right:0;top:190px;text-align:center;font-size:44px;font-weight:500;letter-spacing:.3px}
.hero-text{position:absolute;left:275px;width:500px;top:256px;text-align:center;font-size:9.5px;line-height:1.4;letter-spacing:.3px}
.connect{position:absolute;left:40px;top:245px;font-size:8px;letter-spacing:3px;writing-mode:vertical-rl;transform:rotate(180deg)}
.social-col{position:absolute;left:41px;top:350px;display:flex;flex-direction:column;gap:14px}
.social-col span{width:10px;height:10px;border-radius:50%;border:1.5px solid var(--white)}
.slides{position:absolute;left:975px;top:277px;display:flex;flex-direction:column;gap:14px}
.slides span{width:27px;height:27px;border-radius:50%;border:1px solid var(--white);font-size:8px;display:flex;align-items:center;justify-content:center}
.hero-art{position:absolute;left:170px;top:350px;width:720px;height:276px;border-radius:40px 40px 0 0;background:linear-gradient(90deg,#3f8f3a 0%,#6fb13e 18%,#2a8fd0 42%,#c8473b 55%,#e0a43a 72%,#d99e5c 86%,#5aa83a 100%);opacity:.9}

/* Mobile screens */
.phone{position:absolute;top:720px;width:223px;height:460px;border-radius:26px;background:var(--white);overflow:hidden;box-shadow:0 2px 10px rgba(0,0,0,.12)}
.p1{left:94px}.p2{left:346px}.p3{left:598px}.p4{left:850px}
.band{background:var(--brown);color:var(--white);position:relative}
.m-title{font-family:"Fira Sans",sans-serif;font-weight:500;text-align:center}
.tiny{font-size:4px;line-height:1.4}
.pill{display:inline-block;border-radius:8px;font-family:"Fira Sans",sans-serif;font-weight:700;font-size:4px;padding:3px 8px}
.pill-grey{background:#d9d4cf;color:var(--ink)}
.pill-lime{background:var(--lime);color:var(--ink)}
.pill-white{background:var(--white);color:var(--ink)}
.checks{list-style:none;padding:0 24px;display:flex;flex-direction:column;gap:12px}
.checks li{display:flex;align-items:center;gap:7px;font-family:"Fira Sans",sans-serif;font-weight:600;font-size:4.6px}
.tick{flex:none;width:10px;height:10px;border-radius:50%;background:var(--lime);display:flex;align-items:center;justify-content:center}
.service-card{margin:0 auto;width:132px;height:88px;background:var(--card);border-radius:4px;display:flex;flex-direction:column;align-items:center;justify-content:center;gap:8px}
.service-card p{font-family:"Fira Sans",sans-serif;font-weight:600;font-size:4.2px;text-align:center;width:70px}
.arrows{display:flex;justify-content:center;gap:6px}
.arrow{width:12px;height:12px;border-radius:50%;background:#e3e3e3;display:flex;align-items:center;justify-content:center}
.photo{border-radius:2px}
.portrait{width:110px;height:110px;border-radius:50%;background:radial-gradient(circle at 55% 40%,#d9c3a6,#8d7d72 55%,#c9d62e 90%);margin:0 auto}
</style>
</head>
<body>

<!-- Desktop home -->
<section class="desktop" aria-label="Avaleht arvutis">
  <div class="brand"><span class="brand-dot"></span><span class="brand-name">Vilumetsa<br>Kogumisteenused</span></div>
  <nav class="main-nav"><span>Avaleht</span><span>Kodukliendile</span><span>Ärikliendile</span><span>Klienditugi</span><span>Ettevõttest</span><span>Tule tööle!</span></nav>
  <div class="lang"><span class="flag"></span>ET ▾</div>
  <div class="portal-btn">Sisene E-teenindusse</div>

  <h1 class="hero-title heading">Waste Collection And Recycling</h1>
  <p class="hero-text">We manage waste collection and recycling for 100K+ households and businesses across Estonia. Nam mollis nulla a libero maximus convallis. Donec eget odio hendrerit arcu commodo lobortis vitae eu metus.</p>

  <div class="connect">Connect us</div>
  <div class="social-col"><span></span><span></span><span></span></div>
  <div class="slides"><span>1</span><span>2</span><span>3</span></div>

  <div class="hero-art" role="img" aria-label="Illustration of a blue recycling bin surrounded by bottles, cans, cups, paper, boxes and green leaves"></div>
</section>

<!-- Mobile 1 -->
<section class="phone p1" aria-label="Mobiili avaleht">
  <div class="band" style="height:229px">
    <div style="position:absolute;left:20px;top:16px;width:8px;height:6px;border-top:1px solid #fff;border-bottom:1px solid #fff"></div>
    <div style="position:absolute;right:18px;top:13px;display:flex;align-items:center;gap:3px;font-size:4px;font-weight:700"><span class="flag" style="width:11px;height:11px;border-width:1px"></span>ET ▾</div>
    <div style="position:absolute;left:0;right:0;top:38px;text-align:center;font-family:'Fira Sans',sans-serif;font-size:9px;font-weight:500;line-height:1.1">Vilumetsa<br>Kogumisteenused</div>
    <div class="m-title" style="position:absolute;left:0;right:0;top:90px;font-size:12.5px">Waste Collection And Recycling</div>
    <div class="tiny" style="position:absolute;left:0;right:0;top:108px;text-align:center">We manage waste collection and recycling for 100K+ households</div>
    <div style="position:absolute;left:0;right:0;top:120px;text-align:center"><span class="pill pill-white">Sisene E-teenindusse</span></div>
    <div role="img" aria-label="Illustration of a recycling bin with bottles, packaging and leaves" style="position:absolute;left:22px;right:22px;bottom:0;height:72px;border-radius:20px 20px 0 0;background:linear-gradient(90deg,#4f9e3a,#2a8fd0 45%,#c8473b 58%,#e0a43a 80%,#5aa83a)"></div>
  </div>
  <div style="padding-top:22px">
    <div class="portrait" role="img" aria-label="Portrait photo of a smiling customer"></div>
    <div class="m-title" style="font-size:8px;margin:24px 0 26px">Korraldatud jäätmevedu</div>
    <ul class="checks">
      <li><span class="tick"><svg width="5" height="4" viewBox="0 0 5 4"><path d="M.5 2l1.3 1.3L4.5.6" fill="none" stroke="#fff" stroke-width=".8"/></svg></span>Miks on vaja korraldatud jäätmevedu?</li>
      <li><span class="tick"><svg width="5" height="4" viewBox="0 0 5 4"><path d="M.5 2l1.3 1.3L4.5.6" fill="none" stroke="#fff" stroke-width=".8"/></svg></span>Mida korraldatud jäätmevedu tähendab?</li>
    </ul>
  </div>
</section>

<!-- Mobile 2 -->
<section class="phone p2" aria-label="Korraldatud jäätmevedu">
  <div class="portrait" role="img" aria-label="Portrait photo of a smiling customer" style="margin-top:-40px"></div>
  <div class="m-title" style="font-size:8px;margin:20px 0 26px">Korraldatud jäätmevedu</div>
  <ul class="checks" style="gap:14px">
    <li><span class="tick"><svg width="5" height="4" viewBox="0 0 5 4"><path d="M.5 2l1.3 1.3L4.5.6" fill="none" stroke="#fff" stroke-width=".8"/></svg></span>Miks on vaja korraldatud jäätmevedu?</li>
    <li><span class="tick"><svg width="5" height="4" viewBox="0 0 5 4"><path d="M.5 2l1.3 1.3L4.5.6" fill="none" stroke="#fff" stroke-width=".8"/></svg></span>Mida korraldatud jäätmevedu tähendab?</li>
    <li><span class="tick"><svg width="5" height="4" viewBox="0 0 5 4"><path d="M.5 2l1.3 1.3L4.5.6" fill="none" stroke="#fff" stroke-width=".8"/></svg></span>Kuidas omavalitsus valib vedaja, kellele antakse jäätmeveo ainuõigus?</li>
  </ul>
  <div style="text-align:center;margin:26px 0 26px"><span class="pill pill-grey">Read More</span></div>
  <div class="service-card">
    <svg width="24" height="20" viewBox="0 0 24 20"><rect x="1" y="3" width="14" height="12" rx="2" fill="#cddc2b" stroke="#5e534b" stroke-width="1"/><path d="M15 7h4l4 4v4h-8z" fill="#cddc2b" stroke="#5e534b" stroke-width="1"/><circle cx="6" cy="16" r="2.5" fill="#fff" stroke="#5e534b"/><circle cx="18" cy="16" r="2.5" fill="#fff" stroke="#5e534b"/></svg>
    <p>Mida korraldatud jäätmevedu tähendab?</p>
  </div>
  <div class="arrows" style="margin-top:14px">
    <span class="arrow"><svg width="6" height="4" viewBox="0 0 6 4"><path d="M5.5 2H.8M2 .6L.6 2 2 3.4" fill="none" stroke="#333" stroke-width=".6"/></svg></span>
    <span class="arrow"><svg width="6" height="4" viewBox="0 0 6 4"><path d="M.5 2h4.7M4 .6L5.4 2 4 3.4" fill="none" stroke="#333" stroke-width=".6"/></svg></span>
  </div>
  <div class="band" style="position:absolute;left:0;right:0;bottom:0;height:76px">
    <div class="m-title" style="position:absolute;left:26px;top:36px;font-size:7px">Sustainability</div>
    <div role="img" aria-label="Photo of a tower covered in greenery" style="position:absolute;left:86px;top:0;width:56px;height:76px;background:linear-gradient(#6d8a4a,#3f5a33)"></div>
    <div class="tiny" style="position:absolute;left:150px;top:38px;width:55px">Lorem ipsum dolor sit amet, consectetur adipiscing.</div>
  </div>
</section>

<!-- Mobile 3 -->
<section class="phone p3" aria-label="Teenused ja uudised">
  <div style="text-align:center;margin-top:24px"><span class="pill pill-grey">Read More</span></div>
  <div class="service-card" style="margin-top:24px">
    <svg width="24" height="20" viewBox="0 0 24 20"><rect x="1" y="3" width="14" height="12" rx="2" fill="#cddc2b" stroke="#5e534b" stroke-width="1"/><path d="M15 7h4l4 4v4h-8z" fill="#cddc2b" stroke="#5e534b" stroke-width="1"/><circle cx="6" cy="16" r="2.5" fill="#fff" stroke="#5e534b"/><circle cx="18" cy="16" r="2.5" fill="#fff" stroke="#5e534b"/></svg>
    <p>Mida korraldatud jäätmevedu tähendab?</p>
  </div>
  <div class="band" style="position:absolute;left:0;right:0;top:170px;height:78px">
    <div class="m-title" style="position:absolute;left:16px;top:20px;font-size:5px;text-align:left">Sustainability</div>
    <div class="tiny" style="position:absolute;left:16px;top:28px;color:var(--lime)">Lorem ipsum dolor sit amet</div>
    <div class="tiny" style="position:absolute;left:16px;top:35px;width:62px">Sed do eiusmod tempor incididunt ut labore et dolore magna aliqua.</div>
    <div class="tiny" style="position:absolute;left:16px;top:54px;width:12px;border-bottom:1px solid var(--lime)"></div>
    <div role="img" aria-label="Photo of a tower covered in greenery" style="position:absolute;left:88px;top:-8px;width:54px;height:86px;background:linear-gradient(#6d8a4a,#3f5a33)"></div>
  </div>
  <div style="position:absolute;left:0;right:0;top:248px;height:130px;background:#eef0f0">
    <div class="m-title" style="position:absolute;left:17px;top:44px;font-size:5.5px;text-align:left;font-weight:600">Available on iOS and<br>Android devices.</div>
    <div class="tiny" style="position:absolute;left:17px;top:60px;width:58px;color:var(--muted)">Manage pickups, invoices and schedules from your phone.</div>
    <div role="img" aria-label="Photo of a smartphone showing the self-service app" style="position:absolute;left:84px;top:20px;width:66px;height:100px;border-radius:10px;background:linear-gradient(135deg,#ffffff,#d6dadc);transform:rotate(30deg)"></div>
    <div style="position:absolute;right:16px;top:78px"><span class="pill pill-lime" style="font-size:3px;padding:1px 4px">Download app</span></div>
  </div>
  <div class="m-title" style="position:absolute;left:0;right:0;top:401px;font-size:7.5px">Viimased Uudised</div>
  <div role="img" aria-label="Photo of a gloved hand picking up a plastic bottle in the forest" style="position:absolute;left:45px;top:425px;width:133px;height:40px;background:linear-gradient(90deg,#8da35c,#3f78c9 50%,#a7b47a)"></div>
</section>

<!-- Mobile 4 -->
<section class="phone p4" aria-label="Uudised ja jalus">
  <div class="m-title" style="margin-top:16px;font-size:7.5px">Viimased Uudised</div>
  <div style="position:relative;margin-top:12px;height:88px">
    <span class="arrow" style="position:absolute;left:20px;top:38px;width:11px;height:11px"><svg width="6" height="4" viewBox="0 0 6 4"><path d="M5.5 2H.8M2 .6L.6 2 2 3.4" fill="none" stroke="#333" stroke-width=".6"/></svg></span>
    <div class="photo" role="img" aria-label="Photo of a gloved hand picking up a plastic bottle in the forest" style="position:absolute;left:46px;top:0;width:132px;height:88px;background:linear-gradient(160deg,#b8c6a0,#4a86c9 45%,#5f8a3a)"></div>
    <span class="arrow" style="position:absolute;right:20px;top:38px;width:11px;height:11px"><svg width="6" height="4" viewBox="0 0 6 4"><path d="M.5 2h4.7M4 .6L5.4 2 4 3.4" fill="none" stroke="#333" stroke-width=".6"/></svg></span>
  </div>
  <p style="margin-top:8px;text-align:center;font-family:'Fira Sans',sans-serif;font-weight:600;font-size:4.2px">Tallinna klienditeeninduse lahtiolekuaegade muudatus</p>
  <p class="tiny" style="text-align:center;color:var(--muted);margin-top:6px">14.12.2023</p>
  <div style="text-align:center;margin-top:12px"><span class="pill pill-lime">View More</span></div>
  <footer class="band" style="position:absolute;left:0;right:0;bottom:0;height:256px">
    <div style="position:absolute;left:0;right:0;top:38px;display:flex;justify-content:center;align-items:center;gap:5px"><span style="width:14px;height:14px;border-radius:50%;background:var(--white)"></span><span style="font-family:'Fira Sans',sans-serif;font-size:6.5px;font-weight:500;line-height:1.05">Vilumetsa<br>Kogumisteenused</span></div>
    <p class="tiny" style="position:absolute;left:50px;right:50px;top:66px;text-align:center">Lorem ipsum dolor sit amet, consectetur adipiscing elit. Vivamus et fermentum eros. Nam mollis nulla a libero.</p>
    <div style="position:absolute;left:0;right:0;top:89px;display:flex;justify-content:center;gap:3px"><span style="width:8px;height:8px;border-radius:50%;background:#fff"></span><span style="width:8px;height:8px;border-radius:50%;background:#fff"></span><span style="width:8px;height:8px;border-radius:50%;background:#fff"></span><span style="width:8px;height:8px;border-radius:50%;background:#fff"></span></div>
    <p style="position:absolute;left:0;right:0;top:113px;text-align:center;font-size:4px;font-weight:700">Contact Details</p>
    <div class="tiny" style="position:absolute;left:30px;top:128px;display:flex;gap:10px;font-size:3.4px">
      <span style="display:flex;gap:3px"><svg width="5" height="6" viewBox="0 0 5 6"><path d="M2.5 5.6S.5 3.6.5 2.3a2 2 0 014 0c0 1.3-2 3.3-2 3.3z" fill="none" stroke="#fff" stroke-width=".5"/></svg>Kase tn 12,<br>Tallinn 10115</span>
      <span style="display:flex;gap:3px"><svg width="5" height="5" viewBox="0 0 5 5"><path d="M1 .5l1 1-.6.7a3 3 0 001.4 1.4l.7-.6 1 1-.7.6C2.3 4.6.4 2.7.4 1.2z" fill="none" stroke="#fff" stroke-width=".4"/></svg>+372 555 0142</span>
      <span style="display:flex;gap:3px"><svg width="6" height="5" viewBox="0 0 6 5"><rect x=".3" y=".5" width="5.4" height="4" fill="none" stroke="#fff" stroke-width=".4"/><path d="M.3.5L3 2.8 5.7.5" fill="none" stroke="#fff" stroke-width=".4"/></svg>info@vilumetsa.ee</span>
    </div>
    <p class="tiny" style="position:absolute;left:0;right:0;top:153px;text-align:center;font-size:3.2px">2024 © Vilumetsa Kogumisteenused. All rights reserved.</p>
  </footer>
</section>

</body>
</html>
```